Webdesign für visa-korvenet.org
Kreativer Initialvorschlag, schnelle Umsetzung, flexible Anpassung des Designvorschlags und nette Kommunikation, gerne wieder!
Zielgruppe
Wir vermitteln weltweit Reisegenehmigungen für Geschäfts- und Privatkunden. Auf VISA-Korvenet.org möchten wir auf deutsch, englisch & chinesisch Reisenden bei der Beiholung von Kurzzeit, Work & Travel & diversen Visaarten helfen.
Aufgabenstellung
Der Webseitezweck ist es, dass Besucher bestellen. Dafür muss die Seite attraktiv, einfach bedienbar und das CTA Element "zum Formular" präsent und mehrfach auftauchen.

```html
<!DOCTYPE html>
<html lang="de">
<head>
<meta charset="utf-8">
<title>Visa Korvenet – Anmeldeformular Touristenvisum</title>
<link href="https://fonts.googleapis.com/css2?family=Roboto:wght@400;500;700&family=Lato:wght@300;400&display=swap" rel="stylesheet">
<style>
:root{
  --blue:#0b4f9e;
  --blue-dark:#083f80;
  --red:#c4121a;
  --red-dark:#a50e15;
  --text:#333;
  --muted:#555;
  --field:#e4e4e4;
  --panel:#f7f7f7;
  --panel-line:#dcdcdc;
  --info:#dcebfb;
  --step-off:#b3afaf;
  --white:#fff;
}
*{box-sizing:border-box;margin:0;padding:0}
html,body{width:1200px;height:3426px;overflow:hidden}
body{font-family:"Roboto",Arial,sans-serif;color:var(--text);background:var(--white);position:relative}
.abs{position:absolute}

/* header */
.site-header{left:0;top:0;width:1200px;height:132px;background:linear-gradient(#e4eef9,#f6f9fd)}
.brand-mark{left:37px;top:30px;width:68px;height:68px;border-radius:50%;background:var(--blue)}
.brand-name{left:126px;top:50px;font-size:29px;font-weight:700;color:var(--red)}
.brand-sub{left:127px;top:88px;font-size:12px;color:#333}
.cta-top{left:498px;top:60px;width:307px;height:37px;border-radius:5px;background:var(--red);color:#fff;font-size:14px;font-weight:700;display:flex;align-items:center;justify-content:center;letter-spacing:.2px}
.help{right:38px;text-align:right;font-size:14px;line-height:16px}
.help strong{font-weight:700}
.help .blue{color:var(--blue)}
.help .red{color:var(--red);font-weight:700}
.cards{display:flex;gap:6px;justify-content:flex-end}
.card{width:47px;height:28px;border-radius:3px;font-size:9px;font-weight:700;display:flex;align-items:center;justify-content:center}
.card.c1{background:#2e77bb;color:#fff}
.card.c2{background:#222;color:#fff}
.card.c3{background:#fff;color:var(--blue);border:1px solid #ccc}

/* nav */
.main-nav{left:0;top:132px;width:1200px;height:44px;background:var(--blue);border-bottom:3px solid var(--red)}
.main-nav a{position:absolute;top:0;height:41px;display:flex;align-items:center;color:#fff;font-size:15px;font-weight:500;text-decoration:none}
.main-nav a.active{background:var(--red);padding:0 14px}

/* hero */
.hero{left:0;top:176px;width:1200px;height:234px;background:linear-gradient(90deg,#5e5443 0%,#8d8066 28%,#9fb3b5 48%,#6c7f99 70%,#aab4c6 100%)}
.hero-title{left:37px;top:236px;font-family:"Lato",sans-serif;font-weight:300;font-size:42px;color:#fff}
.hero-box{left:37px;top:298px;width:329px;height:72px;border-radius:6px;background:rgba(0,0,0,.75);color:#fff;font-size:18px;line-height:20px;padding:15px 0 0 29px}

/* intro */
.intro-title{left:35px;top:462px;font-size:33px;font-weight:400;color:#222}
.intro-text{left:37px;top:507px;width:730px;font-size:15px;line-height:19.5px;color:var(--muted)}

/* form panel */
.form-panel{left:37px;top:600px;width:729px;height:2018px;background:var(--panel);border:2px solid #e3e3e3;border-radius:4px}
.section-title{left:89px;font-size:14.5px;font-weight:500;color:#333;display:flex;align-items:center;gap:8px;letter-spacing:.2px}
.section-line{left:89px;width:623px;height:1px;background:var(--panel-line)}
.label{font-size:12px;color:#444}
.label .req{color:var(--red)}
.group-title{left:89px;font-size:14px;font-weight:700;color:#333}
.group-title .req{color:var(--red)}
.field{width:184px;height:28px;background:var(--field)}
.select{width:184px;height:28px;background:var(--field);font-size:12px;color:#444;padding-left:14px;display:flex;align-items:center}
.select::after{content:"";position:absolute;right:15px;top:12px;border:5px solid transparent;border-top:6px solid #333}
.info-box{left:339px;top:718px;width:372px;height:197px;background:var(--info);font-size:12px;line-height:19.3px;color:#333;padding:36px 12px 0 13px}
.info-box::before{content:"";position:absolute;left:-24px;top:86px;border:12px solid transparent;border-right:12px solid var(--info)}
.info-box p{padding-left:7px;text-indent:-7px}
.question{left:89px;width:650px;font-size:12px;line-height:15px;color:#444}
.checkbox{left:89px;top:2436px;width:24px;height:21px;background:var(--field)}
.legal{left:124px;top:2438px;width:628px;font-size:11.3px;line-height:13.7px;color:#444}
.submit{left:93px;top:2544px;width:129px;height:36px;border-radius:5px;background:var(--red);color:#fff;font-size:14px;font-weight:700;display:flex;align-items:center;justify-content:center;box-shadow:0 0 0 2px #e88}

/* steps */
.step{left:820px;width:134px;height:134px;border-radius:50%;color:#fff;font-size:42px;display:flex;align-items:center;justify-content:center}
.step.on{background:var(--blue)}
.step.off{background:var(--step-off)}
.step-label{left:968px;font-size:15px;font-weight:500}
.step-label.on{color:var(--blue)}
.step-label.off{color:#9c9898}

/* callback band */
.callback{left:0;top:2743px;width:1200px;height:220px}
.callback-text{left:37px;top:2840px;width:510px;font-size:13px;line-height:20px;color:#fff}
.cb-label{left:666px;top:2802px;font-size:13px;color:#fff}
.cb-field{height:36px;width:207px;background:#e3eefb;font-size:12px;color:#335;padding-left:12px;display:flex;align-items:center}
.cb-select::after{content:"";position:absolute;right:16px;top:16px;border:5px solid transparent;border-top:6px solid var(--blue)}
.cb-btn{left:886px;top:2878px;width:102px;height:36px;background:var(--red);color:#fff;font-size:12px;font-weight:700;display:flex;align-items:center;justify-content:center}

/* map */
.map{left:0;top:2963px;width:1200px;height:323px;background:linear-gradient(90deg,#e6e3de,#ebe8e2 60%,#dfe7d6)}

/* footer */
.footer{left:0;top:3286px;width:1200px;height:140px;background:var(--blue);border-top:7px solid var(--red)}
.foot-h{font-size:17px;font-weight:500;color:#fff}
.foot-links{font-size:12px;line-height:17.5px;color:#fff}
</style>
</head>
<body>

<header class="abs site-header"></header>
<div class="abs brand-mark"></div>
<div class="abs brand-name">Visa Korvenet</div>
<div class="abs brand-sub">deutsches Formular - Visum Australien</div>
<a class="abs cta-top">JETZT EVISITOR VISUM REGISTRIEREN</a>
<div class="abs help" style="top:24px">
  <strong>Sie brauchen Hilfe?</strong><br>
  Service Hotline von <span class="blue">Mo-Fr 10-16 Uhr</span><br>
  <span class="red">Kostenfrei:</span> <span style="color:var(--red)">0800 5550 2190</span>
  <div class="cards" style="margin-top:6px">
    <span class="card c1">Paxora</span><span class="card c2">Cardelo</span><span class="card c3">Zahlfix</span>
  </div>
</div>

<nav class="abs main-nav">
  <a style="left:49px">STARTSEITE</a>
  <a class="active" style="left:172px">TOURISTEN VISUM</a>
  <a style="left:369px">BUSINESS VISUM</a>
  <a style="left:558px">WAS IST ETA</a>
  <a style="left:698px">AGB</a>
  <a style="left:775px">KONTAKT</a>
</nav>

<div class="abs hero" role="img" aria-label="Foto: Reisepass mit Visum-Stempel"></div>
<h1 class="abs hero-title">ANMELDEFORMULAR</h1>
<div class="abs hero-box">Oder rufen Sie 0800 5550 2190<br>an Telefonisch buchen</div>

<h2 class="abs intro-title">Bewerben Sie sich für Touristenvisum</h2>
<p class="abs intro-text">Füllen Sie unser sicheres Kontaktformular aus, um sich bei visa-korvenet.org zu registrieren. Ein Vertreter von uns wird Sie in Kürze kontaktieren, um Ihnen alle notwendigen Informationen zur Verfügung zu stellen und Ihre Daten zu bestätigen, um Ihre Bewerbung im Gange zu bekommen.</p>

<div class="abs form-panel"></div>

<!-- personal -->
<div class="abs section-title" style="top:643px">
  <svg width="22" height="22" viewBox="0 0 22 22"><circle cx="11" cy="11" r="11" fill="#555"/><circle cx="11" cy="8.5" r="3.6" fill="#f7f7f7"/><path d="M4.5 17.5c1.5-3 4-4 6.5-4s5 1 6.5 4" fill="#f7f7f7"/></svg>
  PERSÖNLICHE DETAILS
</div>
<div class="abs section-line" style="top:683px"></div>

<div class="abs label" style="left:89px;top:715px">Nachname <span class="req">*</span></div>
<div class="abs field" style="left:89px;top:740px"></div>
<div class="abs label" style="left:89px;top:786px">Vorname <span class="req">*</span></div>
<div class="abs field" style="left:89px;top:810px"></div>
<div class="abs label" style="left:89px;top:856px">Früherer Name</div>
<div class="abs field" style="left:89px;top:881px"></div>

<div class="abs info-box">
  <p>- Name vor der Ehe</p>
  <p>- Aliasnamen oder eine alternative Schreibweise Ihres Namens</p>
  <p>- Vatersname (wenn Sie ein russischer Staatsbürger sind)</p>
  <p>- Volle Schreibweise der Initialen Ihrer Namen, die in Ihrem Reisepass eingetragen sind</p>
</div>

<div class="abs group-title" style="top:941px">Geburtstag <span class="req">*</span></div>
<div class="abs label" style="left:89px;top:973px">Tag</div>
<div class="abs label" style="left:301px;top:973px">Monat</div>
<div class="abs label" style="left:511px;top:973px">Jahr</div>
<div class="abs select" style="left:89px;top:995px">1</div>
<div class="abs select" style="left:301px;top:995px">Januar</div>
<div class="abs select" style="left:511px;top:995px">1910</div>

<div class="abs label" style="left:89px;top:1044px">Geburtsland <span class="req">*</span></div>
<div class="abs label" style="left:301px;top:1044px">Staatsangehörigkeit <span class="req">*</span></div>
<div class="abs label" style="left:511px;top:1044px">Weitere Staatsangehörigkeit</div>
<div class="abs select" style="left:89px;top:1066px">Germany (DUE)</div>
<div class="abs select" style="left:301px;top:1066px">Germany (DUE)</div>
<div class="abs select" style="left:511px;top:1066px">Bitte auswählen</div>

<div class="abs label" style="left:89px;top:1115px">Geschlecht &nbsp;<span class="req">*</span></div>
<div class="abs select" style="left:89px;top:1136px">Bitte auswählen</div>

<!-- contact -->
<div class="abs section-title" style="top:1215px">
  <svg width="14" height="20" viewBox="0 0 14 20"><rect width="14" height="20" rx="2" fill="#555"/><circle cx="7" cy="8" r="2.5" fill="#f7f7f7"/><path d="M3 14c1-2 2.5-2.6 4-2.6s3 .6 4 2.6" fill="#f7f7f7"/></svg>
  KONTAKT-DETAILS
</div>
<div class="abs section-line" style="top:1253px"></div>

<div class="abs label" style="left:89px;top:1286px">Land Hauptwohnsitz &nbsp;<span class="req">*</span></div>
<div class="abs label" style="left:301px;top:1286px">Aktuelle Anschrift Straße <span class="req">*</span></div>
<div class="abs label" style="left:511px;top:1286px">Aktuelle Anschrift Postleitzahl <span class="req">*</span></div>
<div class="abs select" style="left:89px;top:1308px">Bitte auswählen</div>
<div class="abs field" style="left:301px;top:1308px"></div>
<div class="abs field" style="left:511px;top:1308px"></div>

<div class="abs label" style="left:89px;top:1359px">Aktuelle Anschrift Ort</div>
<div class="abs label" style="left:301px;top:1359px">Aktuelle Anschrift Bundesland</div>
<div class="abs label" style="left:511px;top:1359px">E-Mail Adresse <span class="req">*</span></div>
<div class="abs field" style="left:89px;top:1381px"></div>
<div class="abs field" style="left:301px;top:1381px"></div>
<div class="abs field" style="left:511px;top:1381px"></div>

<div class="abs label" style="left:89px;top:1430px">Telefonnummer <span class="req">*</span></div>
<div class="abs field" style="left:89px;top:1451px"></div>

<!-- migration -->
<div class="abs section-title" style="top:1523px">
  <svg width="24" height="18" viewBox="0 0 24 18"><rect x="8" y="0" width="8" height="4" rx="1" fill="none" stroke="#555" stroke-width="2"/><rect y="3" width="24" height="15" rx="2" fill="#555"/><rect y="9" width="24" height="1.5" fill="#f7f7f7"/></svg>
  MIGRATIONSDETAILS
</div>
<div class="abs section-line" style="top:1562px"></div>

<div class="abs label" style="left:89px;top:1588px">Reisepassnummer <span class="req">*</span></div>
<div class="abs field" style="left:89px;top:1608px"></div>
<svg class="abs" style="left:283px;top:1611px" width="23" height="23" viewBox="0 0 23 23"><circle cx="11.5" cy="11.5" r="11.5" fill="#1f5fb5"/><circle cx="11.5" cy="6" r="1.8" fill="#fff"/><rect x="9.8" y="9.2" width="3.4" height="9" fill="#fff"/></svg>

<div class="abs group-title" style="top:1666px">Austellungsdatum des Reisepasses <span class="req">*</span></div>
<div class="abs label" style="left:89px;top:1697px">Tag</div>
<div class="abs label" style="left:301px;top:1697px">Monat</div>
<div class="abs label" style="left:511px;top:1697px">Jahr</div>
<div class="abs select" style="left:89px;top:1719px">1</div>
<div class="abs select" style="left:301px;top:1719px">Januar</div>
<div class="abs select" style="left:511px;top:1719px">1910</div>

<div class="abs group-title" style="top:1780px">Ablaufdatum des Reisepasses &nbsp;<span class="req">*</span></div>
<div class="abs label" style="left:89px;top:1812px">Tag</div>
<div class="abs label" style="left:301px;top:1812px">Monat</div>
<div class="abs label" style="left:511px;top:1812px">Jahr</div>
<div class="abs select" style="left:89px;top:1833px">1</div>
<div class="abs select" style="left:301px;top:1833px">Januar</div>
<div class="abs select" style="left:511px;top:1833px">1910</div>

<div class="abs label" style="left:89px;top:1891px">Name der ausstellenden Behörde <span class="req">*</span></div>
<div class="abs label" style="left:301px;top:1891px">Art des Visums &nbsp;<span class="req">*</span></div>
<div class="abs field" style="left:89px;top:1912px"></div>
<div class="abs select" style="left:301px;top:1912px">Bittte wählen -</div>

<div class="abs question" style="top:1970px">Sind Sie frei von Tuberkulose zum Antritt der Reise, bzw. bei der Einreise nach Australien? <span style="color:var(--red)">*</span></div>
<div class="abs select" style="left:89px;top:1993px">Bittte wählen -</div>

<div class="abs question" style="top:2043px">Haben Sie schon einmal eine oder mehrere Straftaten begangen, für die Sie eine Gesamtstrafdauer von 12 Monaten oder mehr, auf Bewährung oder nicht auf Bewährung, verbüßen mussten? <span style="color:var(--red)">*</span></div>
<div class="abs select" style="left:89px;top:2085px">Bittte wählen -</div>

<div class="abs question" style="top:2145px">Möchten Sie länger als 3 Monate in Australien studieren oder sich weiterbilden? <span style="color:var(--red)">*</span></div>
<div class="abs select" style="left:89px;top:2174px">Bittte wählen -</div>

<div class="abs question" style="top:2233px">Wurden Sie jemals angeklagt oder läuft aktuell ein Verfahren gegen Sie? <span style="color:var(--red)">*</span></div>
<div class="abs select" style="left:89px;top:2262px">Bittte wählen -</div>

<div class="abs question" style="top:2320px">Wurden Sie jemals in irgend einem Land angeklagt, auch wenn das Verfahren aus den öffentlichen Registern gelöscht wurde? <span style="color:var(--red)">*</span></div>
<div class="abs select" style="left:89px;top:2365px">Bittte wählen -</div>

<div class="abs checkbox"></div>
<p class="abs legal">Ich bestätige, dass ich mich außerhalb von Australien befinde. Rechtsverzicht: Ich habe alle relevanten Informationen gelesen und bin mir bewusst, dass ich hiermit für die Gültigkeitsdauer meiner Reisegenehmigung, die mir über das Evisitor erteilt wurde, von sämtlichen Rechten auf Revision oder Einspruch gegen die Entscheidung hinsichtlich meiner Einreiseberechtigung durch den Beamten der Zoll- und Grenzschutzbehörde Australiens und, außer im Rahmen eines Antrags auf Asyl, auf eine Anfechtung jeder Abschiebeaktion, die aus einem Antrag auf Einreise im Rahmen des eVisitor Programms resultiert, zurücktrete. * *</p>
<a class="abs submit">ABSCHICKEN</a>

<!-- steps -->
<div class="abs step on" style="top:601px">1</div>
<div class="abs step-label on" style="top:659px">FORMULAR AUSFÜLLEN</div>
<div class="abs step off" style="top:759px">2</div>
<div class="abs step-label off" style="top:817px">ANTRAG ÜBERPRÜFEN</div>
<div class="abs step off" style="top:918px">3</div>
<div class="abs step-label off" style="top:976px">BEZAHLEN</div>

<!-- callback band -->
<svg class="abs callback" viewBox="0 0 1200 220" preserveAspectRatio="none">
  <rect width="1200" height="220" fill="var(--blue)"/>
  <polygon points="0,0 661,0 556,220 0,220" fill="var(--red-dark)"/>
</svg>
<p class="abs callback-text">Möchten Sie mit einem unserer Berater über das Telefon sprechen? Bitte reichen Sie Ihre Daten ein und wir werden uns in Kürze melden. Sie können uns auch mailen, wenn Sie es vorziehen würden.</p>
<div class="abs cb-label">Ich möchte gerne diskutieren:</div>
<div class="abs cb-field cb-select" style="left:666px;top:2830px">Touristen Visum</div>
<div class="abs cb-field" style="left:886px;top:2830px">Full Name</div>
<div class="abs cb-field" style="left:666px;top:2878px">Phone Number</div>
<a class="abs cb-btn">RUF MICH AN</a>

<div class="abs map" role="img" aria-label="Stadtplan mit Standort des Büros"></div>

<footer class="abs footer"></footer>
<div class="abs foot-h" style="left:36px;top:3308px">Informationen</div>
<div class="abs foot-links" style="left:36px;top:3338px">Gültigkeitsdauer Visa Korvenet</div>
<div class="abs foot-h" style="left:299px;top:3308px">Quicklinks</div>
<div class="abs foot-links" style="left:299px;top:3338px">Visa Formular deutsch<br>Was ist ETA<br>Touristen Visum<br>Business Visum</div>
<div class="abs foot-links" style="left:458px;top:3338px">Was ist ETA<br>AGB<br>Kontakt</div>
<div class="abs foot-h" style="left:625px;top:3308px">Weiteres</div>
<div class="abs foot-links" style="left:625px;top:3338px">Datenschutz<br>AGB<br>Impressum</div>
<div class="abs help" style="top:3310px;color:#fff">
  <strong>Sie brauchen Hilfe?</strong><br>
  Service Hotline von Mo-Fr 10-16 Uhr<br>
  <strong>Kostenfrei:</strong> 0800 5550 2190
  <div class="cards" style="margin-top:6px">
    <span class="card c1">Paxora</span><span class="card c2">Cardelo</span><span class="card c3">Zahlfix</span>
  </div>
</div>

</body>
</html>
```